Professional business podcast cover

Hey guys,

I want to redesign my podcast cover from the Vimpa Podcast.

It is a professional business podcast for small and medium sized business. Therefor I need something professional.
No fancy glitter designs.
Something real clean and easy.

I am thinking about something similar to this pic.
https://snapvault.example/7Qk2Lm9xP4aZ

What is important for the design?

1. professional and clean look
2. fonts= roboto
3. the logo must be readable also on small devices (please do not change the existing logo!)
4. same color as the logo
5. my full name must be included in the design: Joss Belder

Thank you for your work.

I can not wait to get your designs.

Regards

Joss from Vimpa

Reason: I need a perfect fitting timeless design. If it needs more time to be generated, than we do so.

Target Market(s)

Small and medium sized CEOs

Industry/Entity Type

Consulting

Font styles to use
Sans Serif

Colors
acd136

Requirements
Must have
• 1. professional and clean look
• 2. fonts= roboto
• 3. the logo must be readable also on small devices
• 4. same color as the logo
• 5. size 1400x 1400
• 6. Text: Joss Belder very present
Nice to have
• Get inspired by covers like Dale Korvin, Gus Pellmore or Neil Ostrands podcast.
• https://snapvault.example/4Rb8Tn2wQ6cY
• https://snapvault.example/9Hd3Vj5sK1eX
• https://snapvault.example/2Mf6Pw8uL3gW
Should not have
• Fancy glossi shinny designs

```html
<!DOCTYPE html>
<html lang="de">
<head>
<meta charset="utf-8">
<title>Vimpa Podcast Cover</title>
<link href="https://fonts.googleapis.com/css2?family=Roboto:wght@700;900&display=swap" rel="stylesheet">
<style>
  :root {
    --frame: #ffffff;
    --night: #070b14;
    --steel: #1d3a5c;
    --brand-green: #acd136;
    --band: rgba(0, 0, 0, 0.86);
    --type-light: #ffffff;
  }
  html, body {
    margin: 0;
    padding: 0;
    width: 1200px;
    height: 1200px;
    overflow: hidden;
    background: var(--frame);
  }
  .cover {
    position: absolute;
    left: 38px;
    top: 38px;
    width: 1124px;
    height: 1124px;
    overflow: hidden;
    background:
      radial-gradient(ellipse 70% 60% at 15% 35%, #2c5680 0%, var(--steel) 40%, rgba(13, 24, 40, 0) 80%),
      linear-gradient(90deg, #17304d 0%, #0d1828 55%, var(--night) 100%);
  }
  .host-portrait {
    position: absolute;
    left: 218px;
    top: 46px;
    width: 906px;
    height: 1078px;
    background:
      radial-gradient(ellipse 28% 30% at 65% 38%, #c99680 0%, rgba(201, 150, 128, 0.5) 55%, rgba(201, 150, 128, 0) 100%),
      radial-gradient(ellipse 55% 45% at 65% 100%, #1b2233 0%, #141a29 60%, rgba(20, 26, 41, 0) 100%);
  }
  .host-name {
    position: absolute;
    left: 50px;
    top: 530px;
    margin: 0;
    font-family: "Roboto", sans-serif;
    font-weight: 700;
    font-size: 48px;
    line-height: 1;
    letter-spacing: 2px;
    color: var(--type-light);
    text-transform: uppercase;
  }
  .brand-name {
    position: absolute;
    left: 44px;
    top: 584px;
    margin: 0;
    font-family: "Roboto", sans-serif;
    font-weight: 900;
    font-size: 231px;
    line-height: 1;
    letter-spacing: -4px;
    color: var(--brand-green);
  }
  .tagline-band {
    position: absolute;
    left: 0;
    top: 800px;
    width: 1124px;
    height: 186px;
    background: var(--band);
  }
  .tagline {
    position: absolute;
    left: 46px;
    top: 5px;
    margin: 0;
    font-family: "Roboto", sans-serif;
    font-weight: 700;
    font-size: 70px;
    line-height: 86px;
    letter-spacing: 1px;
    color: var(--type-light);
    text-transform: uppercase;
    white-space: nowrap;
  }
</style>
</head>
<body>
  <main class="cover">
    <div class="host-portrait" role="img" aria-label="Portrait photo of the host in a dark suit, white shirt and green tie"></div>
    <p class="host-name">Joss Belder</p>
    <h1 class="brand-name">VIMPA</h1>
    <div class="tagline-band">
      <p class="tagline">Unternehmerwissen<br>umsetzbar in 15 Minuten</p>
    </div>
  </main>
</body>
</html>
```